Business card, envelope and stationary for attorney / law firm
Law firm: Business card, envelope and stationary
Business card, envelope and stationary for attorney / law firm -
Creative Brief
Professional
Morton L. Viskell
Attorney at Law
4718 Brindlewood Court, Suite 300 San Jose, CA 95110
mlviskell@viskellpatentfirm.example
WWW.VISKELLPATENTFIRM.EXAMPLE

```html
<!DOCTYPE html>
<html lang="en">
<head>
<meta charset="utf-8">
<title>Viskell Patent Firm – Stationery Set</title>
<link rel="stylesheet" href="https://fonts.googleapis.com/css2?family=Open+Sans:wght@400;600;700&display=swap">
<style>
  :root{
    --wine:#7b1014;
    --gold:#c9a55c;
    --paper:#ffffff;
    --ink:#5e5e5e;
    --edge:#b9b9b9;
    --canvas:#ffffff;
  }
  *{box-sizing:border-box;margin:0;padding:0}
  html,body{width:1200px;height:1102px;overflow:hidden;background:var(--canvas)}
  body{position:relative;font-family:"Open Sans",Arial,sans-serif;color:var(--ink)}
  .sheet{position:absolute;background:var(--paper);border:1.5px solid var(--edge);overflow:hidden}
  .sheet > svg.band{position:absolute;inset:0;width:100%;height:100%}
  .brand{position:absolute;display:flex;align-items:center;gap:12px}
  .brand-dot{width:34px;height:34px;border-radius:50%;background:var(--wine);flex:none}
  .brand-name{font-weight:600;color:var(--wine);letter-spacing:2px;line-height:1.15;font-size:20px;text-transform:uppercase}
  .contact{position:absolute;font-size:13px;line-height:1.6;color:var(--ink)}
  .contact .lbl{color:var(--wine);font-weight:600}
  .contact .web{color:var(--wine);font-weight:600}

  .letterhead{left:8px;top:8px;width:880px;height:1086px}
  .letterhead .brand{left:40px;top:52px}
  .letterhead .contact{left:40px;top:1000px}

  .biz-label{position:absolute;left:1018px;top:40px;font-size:22px;font-weight:600;color:#222}
  .biz-card{left:650px;top:118px;width:540px;height:325px;box-shadow:0 0 0 1px #ddd}
  .biz-card .holder{position:absolute;right:28px;top:40px;text-align:right;color:#fff}
  .holder .person{font-size:23px;font-weight:700}
  .holder .role{font-size:15px}
  .biz-card .brand{left:30px;top:118px}
  .biz-card .brand-name{font-size:18px}
  .biz-card .contact{left:30px;top:212px}

  .envelope{position:absolute;left:350px;top:474px;width:835px;height:508px}
  .envelope svg.flap{position:absolute;left:0;top:0;width:835px;height:122px}
  .flap-dot{position:absolute;left:403px;top:26px;width:30px;height:30px;border-radius:50%;background:var(--wine)}
  .envelope-body{left:0;top:114px;width:835px;height:394px}
  .envelope-body .brand{left:48px;top:120px}
  .envelope-body .contact{left:48px;top:340px;font-size:12px}
</style>
</head>
<body>

<section class="sheet letterhead" aria-label="Letterhead">
  <svg class="band" viewBox="0 0 880 1086" preserveAspectRatio="none">
    <path d="M170 0 H880 V350 C720 160 430 40 170 0 Z" fill="var(--wine)"/>
    <path d="M170 0 C430 40 720 160 880 350" fill="none" stroke="var(--gold)" stroke-width="5"/>
  </svg>
  <div class="brand"><span class="brand-dot"></span><span class="brand-name">Viskell<br>Patent Firm LLC</span></div>
  <div class="contact">
    4718 Brindlewood Court, Suite 300 San Jose, CA 95110<br>
    <span class="lbl">Tel:</span> 408.555.0142 <span class="lbl">Fax:</span> 408.555.0187<br>
    <span class="web">www.viskellpatentfirm.example</span>
  </div>
</section>

<div class="biz-label">Biz Card</div>
<section class="sheet biz-card" aria-label="Business card">
  <svg class="band" viewBox="0 0 540 325" preserveAspectRatio="none">
    <path d="M0 8 C250 20 440 120 540 300 V0 H0 Z" fill="var(--wine)"/>
    <path d="M0 8 C250 20 440 120 540 300" fill="none" stroke="var(--gold)" stroke-width="4"/>
  </svg>
  <div class="holder">
    <div class="person">Morton L. Viskell</div>
    <div class="role">Attorney at Law</div>
  </div>
  <div class="brand"><span class="brand-dot"></span><span class="brand-name">Viskell<br>Patent Firm LLC</span></div>
  <div class="contact">
    4718 Brindlewood Court, Suite 300 San Jose, CA 95110<br>
    <span class="lbl">Tel:</span> 408.555.0142 &nbsp;<span class="lbl">Fax:</span> 408.555.0187<br>
    mlviskell@viskellpatentfirm.example<br>
    <span class="web">WWW.VISKELLPATENTFIRM.EXAMPLE</span>
  </div>
</section>

<section class="envelope" aria-label="Envelope">
  <svg class="flap" viewBox="0 0 835 122">
    <path d="M1 121 L417 2 L834 121" fill="var(--paper)" stroke="var(--edge)" stroke-width="1.5"/>
  </svg>
  <span class="flap-dot"></span>
  <div class="sheet envelope-body">
    <svg class="band" viewBox="0 0 835 394" preserveAspectRatio="none">
      <path d="M60 0 H835 V300 C640 110 330 20 60 0 Z" fill="var(--wine)"/>
      <path d="M60 0 C330 20 640 110 835 300" fill="none" stroke="var(--gold)" stroke-width="5"/>
    </svg>
    <div class="brand"><span class="brand-dot"></span><span class="brand-name">Viskell<br>Patent Firm LLC</span></div>
    <div class="contact">4718 Brindlewood Court, Suite 300 San Jose, CA 95110</div>
  </div>
</section>

</body>
</html>
```